Mallowick Cellars Premium E-Liquid

We need a business card design, and soon web design/flyers/brochures for a new ELiquid line (for the vaping/ecig market) called Mallowick Cellars. Attached is the basis of our logo and also the "label" that goes on our bottle. Our first flavor out is T'Dova. The Final design should be reminiscent of a fine wine label / Whiskey label, that communicates an elegant experience. The information on these cards is strictly generic / wholesale information and will be included in samples sent to shops.

Target Market(s)

E cigarettes / Vaping / Middle to upper class

Industry/Entity Type

Business

Contact Information for Business Card

Would like to include Darren Plumbley as Founder. Contact is Darren@mallowickcellars-example.com as well as the website of www.mallowickcellars-example.com and a phone number of (555) 817-2649

Number of Pages Required

2 page

Requirements
Must have
• I think the original font in our PSD attached file is what we want across the board. Think "old school tonic" or "Wine labels". Classy/elegant/"high end".
Nice to have
• Would also like to do a card in the same finished design but it would strictly have the company and whole sale information. This would be sent out with samples.
• And then say for wholesale contact sales: sales@mallowickcellars-example.com or visit mallowickcellars-example.com

```html
<!DOCTYPE html>
<html lang="en">
<head>
<meta charset="utf-8">
<title>Mallowick Cellars – Business Card</title>
<link rel="stylesheet" href="https://fonts.googleapis.com/css2?family=Lora:wght@400&family=Lato:wght@400;700&display=swap">
<style>
  :root {
    --backdrop: #2a2a2a;
    --card: #141414;
    --card-panel: #1c1c1c;
    --silver: #d9d9d9;
    --silver-soft: #bdbdbd;
    --rule: #c8c8c8;
  }
  * { box-sizing: border-box; margin: 0; padding: 0; }
  html, body {
    width: 1200px; height: 900px; overflow: hidden;
    background: var(--backdrop);
  }
  .stage {
    position: relative; width: 1200px; height: 900px;
    display: flex; align-items: center; justify-content: center; gap: 60px;
  }
  .card {
    position: relative; width: 510px; height: 292px;
    background: var(--card); border-radius: 26px; overflow: hidden;
    box-shadow: 0 10px 30px rgba(0,0,0,.45);
  }
  /* Contact side */
  .card-back .contact-panel {
    position: absolute; top: 0; right: 0; bottom: 0; width: 250px;
    background: var(--card-panel);
  }
  .wordmark-block {
    position: absolute; left: 30px; top: 96px; width: 220px;
    text-align: center;
  }
  .wordmark-block .rule { height: 1px; background: var(--rule); width: 200px; }
  .wordmark-block .rule-top { margin-left: 20px; }
  .wordmark {
    font-family: "Lora", serif; font-weight: 400;
    color: var(--silver); font-size: 23px; line-height: 1.2;
    letter-spacing: 1px; text-transform: uppercase;
    padding: 12px 0;
  }
  .contact {
    position: absolute; left: 278px; top: 44px; right: 10px;
    font-family: "Lato", sans-serif; color: var(--silver);
    white-space: nowrap;
  }
  .contact .name { font-weight: 700; font-size: 19px; }
  .contact .role { font-size: 12.5px; color: var(--silver-soft); margin-top: 2px; }
  .contact .address { font-size: 13px; line-height: 1.35; margin-top: 18px; }
  .contact .lines { font-size: 12px; line-height: 1.55; margin-top: 16px; }
  /* Brand side */
  .card-front { display: flex; align-items: center; justify-content: center; }
  .card-front .wordmark {
    font-size: 34px; text-align: center; line-height: 1.15; letter-spacing: 1.5px;
  }
</style>
</head>
<body>
  <main class="stage">
    <section class="card card-back" aria-label="Business card, contact side">
      <div class="contact-panel"></div>
      <div class="wordmark-block">
        <div class="rule rule-top"></div>
        <h1 class="wordmark">Mallowick<br>Cellars</h1>
        <div class="rule rule-bottom"></div>
      </div>
      <div class="contact">
        <p class="name">Darren Plumbley</p>
        <p class="role">Founder</p>
        <p class="address">12345, Address Goes Here<br>Country Name, 123456.</p>
        <p class="lines">T: (555) 817-2649<br>E: Darren@mallowickcellars-example.com<br>W: www.mallowickcellars-example.com</p>
      </div>
    </section>
    <section class="card card-front" aria-label="Business card, brand side">
      <h2 class="wordmark">Mallowick<br>Cellars</h2>
    </section>
  </main>
</body>
</html>
```